Buch-/E-Book-Cover für Sammlung von positiven Erfahrungen
Zielgruppe
die Zielgruppe sind Väter die ihren Söhne eine Sammlung von Empfehlungen für ein positives Leben schenken sollen. Der Titel des Buches heisst 'Unter hellen Kiefern'
Aufgabenstellung
ich möchte mich hier von den Designern überraschen und inspirieren lassen.

```html
<!DOCTYPE html>
<html lang="de">
<head>
<meta charset="utf-8">
<title>Unter hellen Kiefern – Buchcover</title>
<link rel="stylesheet" href="https://fonts.googleapis.com/css2?family=Oswald:wght@600;700&family=Roboto+Condensed:wght@400&family=Montserrat:wght@500&display=swap">
<style>
  :root {
    --sky-top: #a9dbe6;
    --sky-mid: #9fd2df;
    --haze: #7fb8c8;
    --sea-deep: #1f5f7c;
    --sea-mid: #2d7592;
    --rock: #b79f78;
    --rock-dark: #6f6a4e;
    --ink: #1b1d1f;
    --band: #0e1226;
    --gold: #b8894d;
    --band-text: #f2f2f2;
  }
  * { margin: 0; padding: 0; box-sizing: border-box; }
  html, body {
    width: 930px;
    height: 1200px;
    overflow: hidden;
    background: #ffffff;
  }
  .cover {
    position: relative;
    width: 930px;
    height: 1200px;
    background: linear-gradient(180deg, var(--sky-top) 0%, var(--sky-mid) 45%, var(--haze) 60%);
    overflow: hidden;
  }
  .cover-photo {
    position: absolute;
    left: 0;
    top: 640px;
    width: 930px;
    height: 352px;
    background:
      linear-gradient(180deg, rgba(127,184,200,1) 0%, rgba(127,184,200,0) 22%),
      linear-gradient(180deg, var(--sea-mid) 20%, var(--sea-deep) 55%, var(--rock-dark) 78%, var(--rock) 100%);
  }
  .title-block {
    position: absolute;
    left: 0;
    top: 70px;
    width: 930px;
    text-align: center;
    color: var(--ink);
  }
  .title-small {
    display: flex;
    align-items: center;
    justify-content: center;
    gap: 26px;
    font-family: "Oswald", sans-serif;
    font-weight: 600;
    font-size: 42px;
    letter-spacing: 1px;
    line-height: 1;
  }
  .title-small .rule {
    display: block;
    width: 250px;
    height: 3px;
    background: var(--ink);
  }
  .title-big {
    font-family: "Oswald", sans-serif;
    font-weight: 700;
    font-size: 150px;
    line-height: 1;
    letter-spacing: 2px;
    margin: 8px 0 10px;
  }
  .title-big.last { margin-top: 26px; }
  .title-rule {
    width: 640px;
    height: 3px;
    background: var(--ink);
    margin: 18px auto 0;
  }
  .subtitle {
    margin-top: 22px;
    font-family: "Roboto Condensed", sans-serif;
    font-weight: 400;
    font-size: 30px;
    line-height: 1.15;
    letter-spacing: 0.5px;
  }
  .gold-line {
    position: absolute;
    left: 0;
    top: 992px;
    width: 930px;
    height: 9px;
    background: var(--gold);
  }
  .author-band {
    position: absolute;
    left: 0;
    top: 1001px;
    width: 930px;
    height: 199px;
    background: var(--band);
    display: flex;
    align-items: center;
    justify-content: center;
  }
  .author {
    font-family: "Montserrat", sans-serif;
    font-weight: 500;
    font-size: 40px;
    letter-spacing: 6px;
    color: var(--band-text);
  }
</style>
</head>
<body>
  <main class="cover">
    <div class="cover-photo" role="img" aria-label="Foto: Vater und Sohn mit Rucksäcken auf einer Klippe, Blick über das Meer und die Küste"></div>

    <header class="title-block">
      <div class="title-small"><span class="rule"></span><span>UNTER</span><span class="rule"></span></div>
      <h1 class="title-big">HELLEN</h1>
      <div class="title-small"><span class="rule"></span><span class="rule"></span></div>
      <div class="title-big last">KIEFERN</div>
      <div class="title-rule"></div>
      <p class="subtitle">EINE SAMMLUNG VON EMPFEHLUNGEN<br>FÜR EIN POSITIVES LEBEN</p>
    </header>

    <div class="gold-line"></div>
    <footer class="author-band">
      <p class="author">JONAS WENDTLAND</p>
    </footer>
  </main>
</body>
</html>
```